Stationary/business card/envelope design for Larkvale Dentalcare

We are located in the foothills of the sierra nevada mountains. We are looking for a beautiful classy modern stationary. We need evelopes and business card design all to flow seamlessly. Envelope design.

Additional office address 4816 Meridian Wy., Suite B, Auburn, CA 95604 Phone: pending Fax: pending.

3 different Drs on each business card:
Helen R. Marsh, DDS
Orla P. Marsh, DDS
Rebecca S. Halvey, DDS

Target Market(s)

Dental patients

Industry/Entity Type

Dental

Contact Information for Business Card

Two sided. See example.

Font styles to use
Sans Serif

Requirements
Must have
• One sided business cards. Need envelope design.
Colors should match existing logo.

Helen R. Marsh, DDS
Orla P. Marsh, DDS
Rebecca S. Halvey, DDS

```html
<!DOCTYPE html>
<html lang="en">
<head>
<meta charset="utf-8">
<title>Larkvale Dentalcare Stationery</title>
<link href="https://fonts.googleapis.com/css2?family=Lato:wght@400;700&display=swap" rel="stylesheet">
<style>
:root{
  --green:#1c7a34;
  --green-dark:#17692c;
  --blue:#3cb8dd;
  --blue-soft:#47bee0;
  --ink:#2a2a2a;
  --muted:#555;
  --paper:#ffffff;
  --bg:#e4e4e4;
  --label:#8a8a8a;
}
*{box-sizing:border-box;margin:0;padding:0}
html,body{width:1200px;height:769px;overflow:hidden;background:var(--bg)}
body{position:relative;font-family:'Lato',sans-serif;color:var(--ink)}
.sheet{position:absolute;background:var(--paper);overflow:hidden;box-shadow:0 2px 6px rgba(0,0,0,.18)}
.wave{position:absolute;left:0;bottom:0;width:100%;display:block}
.brand{display:flex;align-items:center;gap:6px}
.brand-dot{border-radius:50%;background:var(--blue);flex:none}
.brand-name{color:var(--green);font-weight:700;line-height:1.1}
.band-text{position:absolute;color:#fff;white-space:nowrap}

/* letterhead */
.letterhead{left:86px;top:99px;width:438px;height:561px}
.letterhead .brand{position:absolute;left:41px;top:22px}
.letterhead .brand-dot{width:40px;height:40px}
.letterhead .brand-name{font-size:14px;width:90px}
.contact{position:absolute;left:259px;top:14px;border-left:1px solid #999;padding-left:6px;font-size:8.5px;line-height:10.2px;list-style:none}
.contact li{display:flex;align-items:center;gap:4px}
.icon{width:7px;height:7px;flex:none}
.letter{position:absolute;left:42px;top:102px;width:354px;font-size:7px;line-height:9px;color:#444}
.letter p{margin-bottom:0}
.letter .date{margin-bottom:8px}
.letter .recipient{margin-bottom:24px;line-height:8.4px}
.letter .greeting{margin-bottom:12px}
.letter .body{line-height:12.6px;text-align:justify;margin-bottom:12.6px}
.letter .closing{margin-top:24px}
.signature{display:block;width:100px;height:16px;margin:6px 0 6px;background:linear-gradient(90deg,#e8e8e8,#f4f4f4)}
.signer{font-size:9px;font-weight:700;color:#333;line-height:12px}
.signer-role{font-size:7.5px;color:#444}
.letterhead .band-text{right:48px;bottom:20px;font-size:8.5px}

/* envelope */
.envelope-label{position:absolute;left:814px;top:126px;font-size:18px;color:var(--label);letter-spacing:.3px}
.envelope{left:597px;top:171px;width:508px;height:229px}
.envelope .brand{position:absolute;left:36px;top:46px}
.envelope .brand-dot{width:42px;height:42px}
.envelope .brand-name{font-size:14px;width:92px}
.envelope .band-text{right:47px;bottom:20px;font-size:8.5px}

/* business card */
.card{left:607px;top:487px;width:234px;height:138px}
.doctor{position:absolute;left:11px;top:14px}
.doctor-name{font-size:10.5px;font-weight:700;color:var(--green);line-height:12px}
.doctor-role{font-size:6.5px;color:#333}
.card-address{position:absolute;left:11px;top:59px;font-size:6.4px;line-height:8.2px;color:#333}
.card-contact{position:absolute;left:11px;top:82px;font-size:6.4px;line-height:8.2px;list-style:none;color:#333}
.card-contact li{display:flex;align-items:center;gap:3px}
.card-contact .icon{width:5.5px;height:5.5px}
.card .brand{position:absolute;left:148px;top:22px;flex-direction:column;gap:4px}
.card .brand-dot{width:38px;height:38px}
.card .brand-name{font-size:10px;text-align:center;width:74px}
.card .band-text{right:16px;bottom:9px;font-size:6.4px}

/* appointment card */
.appointment{left:862px;top:487px;width:234px;height:138px}
.appt-head{height:37px;background:var(--blue);color:#fff;font-size:10px;display:flex;align-items:center;justify-content:center;padding-top:2px}
.appt-fields{font-size:7.5px;color:#444;text-align:center;margin-top:17px}
.days{display:flex;justify-content:center;gap:6px;margin-top:9px;font-size:6.8px;color:#444}
.day{display:flex;align-items:center;gap:2px}
.box{width:8px;height:8px;border:1px solid #555}
.appt-foot{position:absolute;left:0;bottom:0;width:100%;height:42px;background:var(--blue);color:#fff;font-size:7.4px;display:flex;align-items:center;justify-content:center}
</style>
</head>
<body>

<svg width="0" height="0" style="position:absolute" aria-hidden="true">
  <defs>
    <symbol id="swoosh" viewBox="0 0 876 150" preserveAspectRatio="none">
      <path d="M0,48 C160,100 320,98 520,58 C660,28 790,10 876,20 L876,150 L0,150 Z" fill="#3cb8dd"/>
      <path d="M0,0 C120,58 260,92 525,38 C300,86 140,82 0,36 Z" fill="#1c7a34"/>
    </symbol>
    <symbol id="i-phone" viewBox="0 0 10 10"><path d="M2,1 L4,1 L5,3 L4,4 C4.5,5.3 5,5.8 6,6 L7,5 L9,6 L9,8 C9,8.6 8.5,9 8,9 C4,9 1,6 1,2 C1,1.4 1.4,1 2,1 Z" fill="#1c7a34"/></symbol>
    <symbol id="i-fax" viewBox="0 0 10 10"><rect x="2.5" y="1" width="5" height="3" fill="#1c7a34"/><rect x="1" y="4" width="8" height="4" rx="1" fill="#1c7a34"/><rect x="2.5" y="7" width="5" height="2.5" fill="#1c7a34"/></symbol>
    <symbol id="i-mail" viewBox="0 0 10 10"><rect x="0.5" y="2" width="9" height="6.5" fill="#1c7a34"/><path d="M0.5,2 L5,6 L9.5,2" fill="none" stroke="#fff" stroke-width=".8"/></symbol>
    <symbol id="i-web" viewBox="0 0 10 10"><circle cx="5" cy="5" r="4.2" fill="none" stroke="#1c7a34" stroke-width="1"/><ellipse cx="5" cy="5" rx="1.8" ry="4.2" fill="none" stroke="#1c7a34" stroke-width=".8"/><path d="M1,5 H9 M1.7,3 H8.3 M1.7,7 H8.3" stroke="#1c7a34" stroke-width=".7"/></symbol>
  </defs>
</svg>

<section class="sheet letterhead">
  <div class="brand"><span class="brand-dot"></span><span class="brand-name">Larkvale Dentalcare</span></div>
  <ul class="contact">
    <li><svg class="icon"><use href="#i-phone"/></svg>044-318 520 746</li>
    <li><svg class="icon"><use href="#i-fax"/></svg>044-318 520 746</li>
    <li><svg class="icon"><use href="#i-mail"/></svg>larkvaledentalcare@mailhub.com</li>
    <li><svg class="icon"><use href="#i-web"/></svg>www.larkvaledentalcare.com</li>
  </ul>
  <div class="letter">
    <p class="date">Issuing Date: May 5, 2018</p>
    <p class="recipient">Name Of Employee Mr. XYZABC<br>Address of Employee<br>Address Line 2 etc..</p>
    <p class="greeting">Dear Mr.XYZABC</p>
    <p class="body">Lorem Ipsum has been the industry's standard dummy text ever since the 1500s, when an unknown printer took a galley of type and scrambled it to make a type specimen book. It has survived not only five centuries, but also the leap into electronic typesetting, remaining essentially unchanged. It was popularised in the 1960s with the release of Letraset sheets containing Lorem Ipsum passages, and more recently with desktop publishing software like Aldus PageMaker including versions of Lorem Ipsum.</p>
    <p class="body">Lorem Ipsum is simply dummy text of the printing and typesetting industry. Lorem Ipsum has been the industry's standard dummy text ever since the 1500s, when an unknown printer took a galley of type and scrambled it to make a type specimen book.</p>
    <p class="body">It has survived not only five centuries, but also the leap into electronic typesetting, remaining essentially unchanged. It was popularised in the 1960s with the release of Letraset sheets containing Lorem IpsumIpsum passages.</p>
    <p class="closing">Yours Sincerely</p>
    <span class="signature" role="img" aria-label="Handwritten signature"></span>
    <p class="signer">Marcus Dellaway</p>
    <p class="signer-role">Managing Director</p>
  </div>
  <svg class="wave" width="438" height="75"><use href="#swoosh"/></svg>
  <p class="band-text">4816 Meridian Wy., Suite B, Auburn, CA 95604</p>
</section>

<p class="envelope-label">Envelope</p>
<section class="sheet envelope">
  <div class="brand"><span class="brand-dot"></span><span class="brand-name">Larkvale Dentalcare</span></div>
  <svg class="wave" width="508" height="80"><use href="#swoosh"/></svg>
  <p class="band-text">4816 Meridian Wy., Suite B, Auburn, CA 95604</p>
</section>

<section class="sheet card">
  <div class="doctor">
    <p class="doctor-name">Helen R. Marsh, DDS</p>
    <p class="doctor-role">Family &amp; Cosmetic Dentistry</p>
  </div>
  <p class="card-address">4816 Meridian Wy., Suite B,<br>Auburn, CA 95604</p>
  <ul class="card-contact">
    <li><svg class="icon"><use href="#i-phone"/></svg>044-318 520 746</li>
    <li><svg class="icon"><use href="#i-fax"/></svg>044-318 520 746</li>
    <li><svg class="icon"><use href="#i-mail"/></svg>larkvaledentalcare@mailhub.com</li>
  </ul>
  <div class="brand"><span class="brand-dot"></span><span class="brand-name">Larkvale Dentalcare</span></div>
  <svg class="wave" width="234" height="32"><use href="#swoosh"/></svg>
  <p class="band-text">www.larkvaledentalcare.com</p>
</section>

<section class="sheet appointment">
  <div class="appt-head">Your Next Appointment on</div>
  <p class="appt-fields">Date : ...................... Time : ..................... AM / PM</p>
  <div class="days">
    <span class="day"><span class="box"></span>MON</span>
    <span class="day"><span class="box"></span>TUE</span>
    <span class="day"><span class="box"></span>WED</span>
    <span class="day"><span class="box"></span>THU</span>
    <span class="day"><span class="box"></span>FRI</span>
  </div>
  <div class="appt-foot">If unable to keep appointment, kindly give 24hrs notice.</div>
</section>

</body>
</html>
```